Health Coaching Brochure for Healthcare Practioners

I am looking to have a tri-fold brochure created marketed towards healthcare practitioners (doctors, nurses, surgeons, etc), to get them to purchase 1-on-1 health coaching from me.
I've provided the text/content (in pdf & pages), my logo, a picture of me, and two color palettes, but please also include lots of white space. I would like to design to be very clean, modern & crisp. Also include additional photos, of doctors, etc taking care of themselves & feeling happy (maybe eating healthy, maybe exercising, feeling good & happy!)
Please also see http://tallbirchwellness.com and http://instagram.com/tallbirchwellness for a feel of my brand.
Thank you!
Target Market(s)
Healthcare Practioners (mainly based in Los Angeles, for now)
Industry/Entity Type
Healthcare
Look and feel
Each slider illustrates characteristics of the customer's brand and the style your logo design should communicate.

```html
<!DOCTYPE html>
<html lang="en">
<head>
<meta charset="utf-8">
<title>Tall Birch Wellness – Tri-fold Brochure</title>
<link rel="stylesheet" href="https://fonts.googleapis.com/css2?family=Source+Sans+3:wght@300;400;600;700&display=swap">
<style>
  :root {
    --canvas: #e6e6e6;
    --ink: #000000;
    --white: #ffffff;
    --lime: #b5d14f;
    --lime-soft: #a9c64a;
    --green-deep: #1f5e22;
    --green-mid: #3f8a32;
  }
  * { margin: 0; padding: 0; box-sizing: border-box; }
  html, body {
    width: 1200px; height: 1200px; overflow: hidden;
    background: var(--canvas);
    font-family: "Source Sans 3", "Myriad Pro", Arial, sans-serif;
  }
  .canvas { position: relative; width: 1200px; height: 1200px; }
  .brochure {
    position: absolute; left: 40px; top: 192px;
    width: 880px; height: 640px;
    transform: scale(1.2727); transform-origin: 0 0;
    box-shadow: 0 2px 6px rgba(0,0,0,.18);
    overflow: hidden;
  }
  .brochure-art { position: absolute; inset: 0; width: 880px; height: 640px; }
  .text { position: absolute; color: var(--white); }

  .bio-name {
    left: 44px; top: 50px;
    font-size: 24.5px; font-weight: 600; letter-spacing: .2px;
    color: var(--lime);
  }
  .bio-intro {
    left: 44px; top: 82px; width: 226px;
    font-size: 10.8px; line-height: 12.6px;
  }
  .bio-story {
    left: 49px; top: 376px; width: 252px;
    font-size: 10.8px; line-height: 12.6px;
  }
  .bio-story p + p { margin-top: 12.6px; }

  .brand-name { font-weight: 700; letter-spacing: .2px; white-space: nowrap; }
  .contact {
    left: 305px; top: 506px; width: 271px; text-align: center;
  }
  .contact .brand-name { font-size: 21px; color: var(--lime); margin-bottom: 6px; }
  .contact-line { font-size: 12px; line-height: 18px; }

  .cover-brand {
    left: 576px; top: 66px; width: 304px; text-align: center;
    font-size: 22px; color: var(--ink);
  }
  .cover-offer {
    left: 576px; top: 525px; width: 290px; text-align: center;
  }
  .offer-title { font-size: 18.5px; font-weight: 700; color: var(--lime); line-height: 22px; }
  .offer-sub { font-size: 18.5px; font-weight: 300; line-height: 21px; }
  .offer-url { font-size: 15px; line-height: 19px; }
</style>
</head>
<body>
<main class="canvas">
  <article class="brochure">
    <svg class="brochure-art" viewBox="0 0 880 640" xmlns="http://www.w3.org/2000/svg">
      <defs>
        <radialGradient id="bioGreen" cx="0.45" cy="0.45" r="0.7">
          <stop offset="0" stop-color="#3e8c33"/>
          <stop offset="1" stop-color="#1b5a1f"/>
        </radialGradient>
        <linearGradient id="coverGreen" x1="0" y1="0" x2="0" y2="1">
          <stop offset="0" stop-color="#b2c95a"/>
          <stop offset="0.35" stop-color="#a9c44f"/>
          <stop offset="0.62" stop-color="#3d8a31"/>
          <stop offset="1" stop-color="#1c5c20"/>
        </linearGradient>
        <radialGradient id="coverGlow" cx="0.5" cy="0.85" r="0.55">
          <stop offset="0" stop-color="#4c9a38"/>
          <stop offset="1" stop-color="#1c5c20" stop-opacity="0"/>
        </radialGradient>
        <linearGradient id="runnerTone" x1="0" y1="0" x2="1" y2="1">
          <stop offset="0" stop-color="#f4f1ea"/>
          <stop offset="0.4" stop-color="#c39a70"/>
          <stop offset="0.7" stop-color="#7a8550"/>
          <stop offset="1" stop-color="#9ab468"/>
        </linearGradient>
        <linearGradient id="trainerTone" x1="0" y1="0" x2="1" y2="1">
          <stop offset="0" stop-color="#f4f0ea"/>
          <stop offset="0.5" stop-color="#dcb39a"/>
          <stop offset="1" stop-color="#d9407e"/>
        </linearGradient>
        <radialGradient id="portraitTone" cx="0.5" cy="0.45" r="0.6">
          <stop offset="0" stop-color="#d6cfc9"/>
          <stop offset="1" stop-color="#5a4a44"/>
        </radialGradient>
      </defs>

      <rect class="panel-base" width="880" height="640" fill="#000"/>

      <!-- middle panel photo -->
      <path d="M305 0 H576 V292 C520 320 470 400 420 430 C380 452 335 448 305 440 Z" fill="url(#runnerTone)" role="img" aria-label="Photo of a runner jogging outdoors on a wooden bridge"/>

      <!-- bio panel green field and arc -->
      <path class="bio-field" d="M0 0 H304 C328 88 296 156 226 210 C156 264 66 324 0 378 Z" fill="url(#bioGreen)"/>
      <path class="bio-band-edge" d="M310 0 C334 92 302 162 232 216 C162 270 72 330 0 384" fill="none" stroke="#fff" stroke-width="22"/>
      <path class="bio-band" d="M310 0 C334 92 302 162 232 216 C162 270 72 330 0 384" fill="none" stroke="var(--lime-soft)" stroke-width="16"/>

      <!-- portrait circle -->
      <circle cx="169" cy="245" r="86" fill="#fff"/>
      <circle cx="169" cy="245" r="82" fill="var(--lime)"/>
      <circle cx="169" cy="245" r="75" fill="#fff"/>
      <circle cx="169" cy="245" r="71" fill="url(#portraitTone)" role="img" aria-label="Portrait photo of the health coach"/>

      <!-- cover panel -->
      <rect x="576" y="0" width="304" height="640" fill="url(#coverGreen)"/>
      <rect x="576" y="300" width="304" height="340" fill="url(#coverGlow)"/>
      <path class="wave-black" d="M576 300 C650 240 720 115 810 110 C845 108 870 112 880 116 V390 C800 405 700 480 576 498 Z" fill="#000"/>
      <path class="wave-white" d="M576 318 C650 258 724 128 812 122 C846 120 870 124 880 128 V378 C800 392 700 468 576 486 Z" fill="#fff"/>
      <path d="M576 324 C652 264 726 134 814 128 C848 126 870 130 880 134 V372 C800 386 700 462 576 480 Z" fill="url(#trainerTone)" role="img" aria-label="Photo of a smiling woman working out with hand weights"/>
    </svg>

    <h1 class="text bio-name">LENA MORAVEC</h1>
    <p class="text bio-intro">is a personal trainer, fitness nutritionist, and holistic health coach based in Los Angeles, California. Lena helps clients improve their health, develop sustainable habits, and achieve their goals to be their best, most vibrant selves.</p>

    <section class="text bio-story">
      <p>Lena sought fitness in 2005 to overcome her lifelong battle of depression, anxiety, and an extra 30 pounds. After completely transforming her body and her mind, she realized that transformation spilling over to other areas of her life – career, relationships, and self-worth. She began to help other people transform their lives, as well.</p>
      <p>Fitness was only the beginning. Lena’s journey has continued to evolve to include a more holistic approach. While getting clients the bodies they want, she puts an even stronger emphasis on health and longevity. She believes proper and efficient digestion is the key to not only getting the body they want, but also to preventing all diseases.</p>
      <p>Studying the latest research, reading and listening to everything health-related, Lena uses that</p>
    </section>

    <section class="text contact">
      <div class="brand-name">tall birch wellness</div>
      <div class="contact-line">lena@tallbirchwellness.com</div>
      <div class="contact-line">www.tallbirchwellness.com</div>
    </section>

    <div class="text cover-brand brand-name">tall birch wellness</div>

    <section class="text cover-offer">
      <div class="offer-title">VIRTUAL GROUP PROGRAM</div>
      <div class="offer-sub">HEAL YOUR GUT</div>
      <div class="offer-url">www.tallbirchwellness.com</div>
    </section>
  </article>
</main>
</body>
</html>
```